Professional Learning Organization for Educators needs a Design Thinking Workshop Flyer

We need a flyer for a series of Introductory Design Thinking workshops we're delivering for education leaders.

We have generated our own version of the flyer with a word template, but want it to look even more professional and eye catching. It is attached.

We had an image that we thought might be good, but pulled it out so we don't bias designers' thinking.
Updates

Reason: We are a bit flexible on the deadline since this is a holiday week and people are traveling

Target Market(s)

Very busy education leaders whose curiosity needs to be stimulated enough to enroll in the course

Industry/Entity Type

Education

Font styles to use
Other font styles liked:
• Century Gothic or something closer to that

Requirements
Must have
• Some version of the text that is on the current flyer that I attached.
Nice to have
• I am very flexible and open right now on this design.

```html
<!DOCTYPE html>
<html lang="en">
<head>
<meta charset="utf-8">
<title>Design Thinking Workshops Flyer</title>
<link href="https://fonts.googleapis.com/css2?family=Roboto+Condensed:wght@400;700&family=Roboto:wght@400;500;700&display=swap" rel="stylesheet">
<style>
  :root {
    --red: #e31e2b;
    --red-dark: #b3101c;
    --blue: #1b8bc6;
    --blue-deep: #0f5a82;
    --navy: #0d3d5c;
    --white: #ffffff;
    --ink: #1f2a33;
    --stage: #e8e6e2;
  }
  * { margin: 0; padding: 0; box-sizing: border-box; }
  html, body { width: 1200px; height: 1200px; overflow: hidden; background: var(--stage); }
  .stage { position: relative; width: 1200px; height: 1200px; }
  .flyer-frame { position: absolute; left: 136px; top: 0; width: 928px; height: 1200px; overflow: hidden; }
  .flyer {
    position: absolute; left: 0; top: 0; width: 1075px; height: 1390px;
    transform: scale(0.86331); transform-origin: 0 0;
    background: var(--white);
    font-family: "Roboto", sans-serif;
  }
  .flyer-art { position: absolute; inset: 0; }

  .brand { position: absolute; right: 58px; top: 92px; display: flex; align-items: flex-start; gap: 14px; }
  .brand-name {
    font-family: "Roboto", sans-serif; font-weight: 700; color: var(--red);
    font-size: 46px; line-height: 1; text-align: right; letter-spacing: 1px;
  }
  .brand-mark { width: 34px; height: 34px; border-radius: 50%; background: var(--blue); margin-top: 8px; }

  .headline { position: absolute; right: 42px; top: 290px; text-align: right;
    font-family: "Roboto Condensed", sans-serif; font-weight: 700; font-size: 58px; line-height: 1.02; }
  .headline .line-one { color: var(--blue); display: block; }
  .headline .line-two { color: var(--red); display: block; }

  .section-bar { position: absolute; left: 0; top: 620px; width: 582px; height: 48px;
    background: linear-gradient(180deg, #f0323e, var(--red-dark));
    border-radius: 0 24px 24px 0; color: var(--white);
    font-family: "Roboto Condensed", sans-serif; font-weight: 700; font-size: 25px;
    line-height: 48px; padding-left: 60px; letter-spacing: .3px; }

  .intro { position: absolute; left: 60px; top: 684px; width: 516px; color: var(--white); font-size: 17px; line-height: 21px; }
  .intro p { text-align: justify; }
  .benefits { list-style: none; margin: 8px 0 10px; }
  .benefits li { position: relative; padding-left: 40px; margin-bottom: 10px; }
  .benefits li::before { content: ""; position: absolute; left: 4px; top: 6px; width: 10px; height: 10px; border-radius: 50%; background: var(--red); }
  .schedule { list-style: none; margin-top: 12px; font-weight: 500; font-size: 21px; line-height: 33.5px; margin-left: -2px; }
  .schedule li { display: flex; align-items: center; gap: 16px; }
  .schedule svg { width: 20px; height: 20px; flex: none; }

  .testimonials { position: absolute; left: 633px; top: 500px; width: 370px; color: var(--white); text-align: center; }
  .testimonials h2 { font-family: "Roboto Condensed", sans-serif; font-weight: 700; font-size: 31px; line-height: 37px; margin-top: 6px; }
  .quote { font-size: 17px; line-height: 21px; padding: 0 32px; }
  .quote.first { margin-top: 12px; }
  .divider { width: 124px; height: 2px; background: var(--white); margin: 14px auto; }
  .contact-title { font-family: "Roboto Condensed", sans-serif; font-weight: 700; font-size: 27px; margin-top: 18px; line-height: 32px; }
  .contact-line { font-size: 22px; line-height: 30px; }
  .contact-title.second { margin-top: 18px; font-size: 29px; }

  .cta { position: absolute; left: 0; width: 1075px; top: 1204px; text-align: center;
    font-family: "Roboto Condensed", sans-serif; color: var(--red); font-size: 37px; line-height: 42px; }
  .cta .url { color: var(--blue); }
  .fine-print { position: absolute; left: 0; width: 1075px; top: 1292px; text-align: center; color: var(--ink); font-size: 21px; font-weight: 500; line-height: 34px; }
  .fine-print span { position: relative; padding-left: 30px; margin: 0 22px; }
  .fine-print span::before { content: ""; position: absolute; left: 0; top: 8px; width: 10px; height: 10px; border-radius: 50%; background: var(--blue); }
</style>
</head>
<body>
<div class="stage">
  <div class="flyer-frame">
    <div class="flyer">
      <svg class="flyer-art" width="1075" height="1390" viewBox="0 0 1075 1390" xmlns="http://www.w3.org/2000/svg">
        <defs>
          <radialGradient id="bodyBlue" cx="0.45" cy="0.45" r="0.7">
            <stop offset="0" stop-color="#1d97cf"/>
            <stop offset="1" stop-color="#0f5a82"/>
          </radialGradient>
          <linearGradient id="cardRed" x1="0" y1="0" x2="0" y2="1">
            <stop offset="0" stop-color="#f02a37"/>
            <stop offset="1" stop-color="#a50e18"/>
          </linearGradient>
          <linearGradient id="footGrey" x1="0" y1="0" x2="0" y2="1">
            <stop offset="0" stop-color="#ffffff"/>
            <stop offset="1" stop-color="#e9e9e9"/>
          </linearGradient>
          <linearGradient id="photoTone" x1="0" y1="0" x2="1" y2="1">
            <stop offset="0" stop-color="#d9c8b8"/>
            <stop offset="0.55" stop-color="#a7a2a6"/>
            <stop offset="1" stop-color="#5c5f6e"/>
          </linearGradient>
        </defs>
        <rect width="1075" height="1390" fill="#f7f7f7"/>
        <path d="M0,545 C260,640 520,590 700,500 C820,470 960,520 1075,560 L1075,1300 L0,1300 Z" fill="url(#bodyBlue)"/>
        <path d="M1003,540 C1030,548 1055,556 1075,566 L1075,600 C1055,590 1030,580 1003,572 Z" fill="var(--red)"/>
        <path d="M1003,580 C1030,590 1055,600 1075,612 L1075,640 C1050,628 1025,618 1003,612 Z" fill="#ffffff"/>
        <path d="M470,522 C560,508 610,494 640,486 L640,499 C600,510 540,522 470,530 Z" fill="var(--red)"/>
        <circle cx="255" cy="240" r="330" fill="#ffffff"/>
        <circle cx="255" cy="240" r="322" fill="var(--red)"/>
        <circle cx="255" cy="240" r="310" fill="var(--navy)"/>
        <circle cx="255" cy="240" r="302" fill="#ffffff"/>
        <circle cx="255" cy="240" r="296" fill="url(#photoTone)" role="img" aria-label="Photo of a thoughtful young educator in glasses at a desk with books"/>
        <path d="M0,1250 Q520,1090 1075,1285 L1075,1390 L0,1390 Z" fill="var(--red)"/>
        <path d="M0,1264 Q520,1110 1075,1302 L1075,1390 L0,1390 Z" fill="url(#footGrey)"/>
        <rect x="633" y="485" width="370" height="632" rx="30" fill="url(#cardRed)"/>
        <path d="M980,485 L1012,485 Q1032,488 1032,510 L1032,545 Q1020,530 1003,532 L1003,500 Z" fill="var(--red-dark)"/>
      </svg>

      <div class="brand">
        <div class="brand-name">COMMON<br>GROUND<br>LAB</div>
        <div class="brand-mark"></div>
      </div>

      <h1 class="headline"><span class="line-one">DESIGN THINKING</span><span class="line-two">WORKSHOPS</span></h1>

      <div class="section-bar">DESIGNING YOUR WAY TO BETTER SOLUTIONS</div>

      <div class="intro">
        <p>Ridgeview Public Schools and Foothill Learning Cooperative invite you to discover the power of Design Thinking. During our three session course, you will learn and practice mindsets and tools that help you continuously and creatively improve the experiences of the people you serve by:</p>
        <ul class="benefits">
          <li>Understanding what your teachers, students and community truly need in their learning and work experiences</li>
          <li>Designing solutions that better meet their needs</li>
          <li>Seeking authentic feedback and reactions to these solutions prior to their implementation.</li>
        </ul>
        <p>We are offering this three-session course at four different times in spring semester. Please choose the course that works best for your schedule.</p>
        <ul class="schedule">
          <li><svg viewBox="0 0 20 20"><path d="M2,11 L8,17 L18,4" fill="none" stroke="#e31e2b" stroke-width="4"/></svg>Monday mornings: 1/23, 1/30 and 2/6</li>
          <li><svg viewBox="0 0 20 20"><path d="M2,11 L8,17 L18,4" fill="none" stroke="#e31e2b" stroke-width="4"/></svg>Tuesday afternoons: 2/7, 2/14 and 2/21</li>
          <li><svg viewBox="0 0 20 20"><path d="M2,11 L8,17 L18,4" fill="none" stroke="#e31e2b" stroke-width="4"/></svg>Wednesday afternoons: 3/8, 3/15 and 3/22</li>
          <li><svg viewBox="0 0 20 20"><path d="M2,11 L8,17 L18,4" fill="none" stroke="#e31e2b" stroke-width="4"/></svg>Wednesday evenings: 2/8, 2/15 and 2/22</li>
        </ul>
      </div>

      <aside class="testimonials">
        <h2>WHAT OUR<br>PARTICIPANTS SAY…</h2>
        <p class="quote first">“This has been an empowering experience that allowed me to try out dramatic changes in my practice that I wouldn’t have imagined before.”</p>
        <div class="divider"></div>
        <p class="quote">“I never realized how often I’ve guessed and assumed what our teachers and students need – now I have a way to stop guessing!”</p>
        <div class="divider"></div>
        <p class="quote">“I finally have tools to generate truly creative ideas that people actually embrace… because they meet their needs”</p>
        <div class="contact-title">FOOTHILL LEARNING CO-OP</div>
        <div class="contact-line">www.foothillcoop.org</div>
        <div class="contact-title second">QUESTIONS?</div>
        <div class="contact-line">j.morgan@ridgeviewsd.org</div>
      </aside>

      <div class="cta">Click here to enroll.<br>Go to <span class="url">www.foothillcoop.org</span> to learn more.</div>
      <div class="fine-print">
        <span>This course is held in Ridgeview Public Schools.</span><span>No fee for RPS leaders</span><br>
        <span>$150 fee for leaders outside of RPS.</span>
      </div>
    </div>
  </div>
</div>
</body>
</html>
```